Smooth on the Corner needs a new flyer

Smooth on the Corner focuses on waxing and is a male and female wax studio (him & her) with colours light grey red white .or open to unisex colours but obviously need to stick to logo attached.. My theme is fun & funky ,.I am thinking cover page and prices on back.i have images that is going on my new website but not sure if i want to keep it easy to focus on prices?
this will go on front ....
First time guest?
Enjoy a complimentry wax ...
for her- indulge in a brow,underarm or bikini line wax
for him-go smooth with a free ear,nose or brow wax

Target Market(s)

18-35

Industry/Entity Type

Beauty Salon

Font styles to use
Sans Serif

Colors
ec1f27
d5d5d5
ffffff

Requirements
Must have
• light grey red and white , fun, unisex
Nice to have
• wow factor
Should not have
• clinical beauty salon feel/ do not favor my current website, i am having it re-done in a fun way.

```html
<!DOCTYPE html>
<html lang="en">
<head>
<meta charset="utf-8">
<title>Smooth on the Corner – First Time Guest Flyer</title>
<link rel="stylesheet" href="https://fonts.googleapis.com/css2?family=Montserrat:wght@400;500;600&display=swap">
<style>
  :root {
    --red: #ec1f27;
    --pink: #f0475e;
    --deep-red: #c8102e;
    --grey: #d5d5d5;
    --light-grey: #eeeeef;
    --white: #ffffff;
    --hanger: #8c8c8c;
  }
  * { margin: 0; padding: 0; box-sizing: border-box; }
  html, body { width: 849px; height: 1200px; overflow: hidden; }
  body { font-family: "Montserrat", Arial, sans-serif; background: var(--white); }

  .flyer {
    position: relative;
    width: 849px;
    height: 1200px;
    overflow: hidden;
    background: linear-gradient(135deg, var(--white) 0%, var(--light-grey) 55%, var(--grey) 100%);
  }

  .hero-photo {
    position: absolute;
    left: 270px;
    top: 0;
    width: 579px;
    height: 720px;
    background: radial-gradient(ellipse at 55% 40%, #d9c9bd 0%, #c7c7cc 45%, rgba(213,213,213,0) 75%);
  }

  .sign {
    position: absolute;
    left: 18px;
    top: 0;
    width: 320px;
    height: 215px;
  }
  .sign-hanger { position: absolute; inset: 0; }
  .sign-board {
    position: absolute;
    left: 0;
    top: 40px;
    width: 320px;
    height: 170px;
    background: var(--white);
    border: 6px solid var(--grey);
    display: flex;
    flex-direction: column;
    align-items: center;
    justify-content: center;
    gap: 12px;
  }
  .brand-name {
    color: var(--red);
    font-weight: 600;
    font-size: 32px;
    line-height: 1.1;
    text-align: center;
  }
  .brand-dot {
    width: 14px;
    height: 14px;
    border-radius: 50%;
    background: var(--red);
  }

  .offer-band { position: absolute; left: 0; top: 0; width: 849px; height: 1200px; }

  .offer {
    position: absolute;
    left: 0;
    top: 800px;
    width: 849px;
    color: var(--white);
  }
  .offer-title {
    text-align: center;
    font-weight: 500;
    font-size: 42px;
    letter-spacing: 5px;
  }
  .offer-subtitle {
    text-align: center;
    font-weight: 400;
    font-size: 24px;
    letter-spacing: 4px;
    margin-top: 8px;
  }
  .offer-list {
    list-style: none;
    margin: 42px 0 0 64px;
    width: 740px;
  }
  .offer-item {
    position: relative;
    padding-left: 34px;
    font-size: 27px;
    font-weight: 500;
    line-height: 1.3;
    margin-bottom: 22px;
  }
  .offer-item::before {
    content: "";
    position: absolute;
    left: 0;
    top: 12px;
    width: 12px;
    height: 12px;
    border-radius: 50%;
    background: var(--white);
  }
</style>
</head>
<body>
<main class="flyer">
  <div class="hero-photo" role="img" aria-label="Smiling couple embracing, woman in a light grey top and man in a light shirt behind her"></div>

  <svg class="offer-band" viewBox="0 0 849 1200" aria-hidden="true">
    <defs>
      <linearGradient id="bandFill" x1="0" y1="0" x2="0" y2="1">
        <stop offset="0" stop-color="#f0475e"/>
        <stop offset="1" stop-color="#ec1f27"/>
      </linearGradient>
    </defs>
    <polygon points="0,670 425,600 849,655 849,1200 0,1200" fill="#ffffff"/>
    <polygon points="0,705 425,640 849,690 849,1200 0,1200" fill="url(#bandFill)"/>
    <polygon points="0,705 425,640 300,760 0,780" fill="#c8102e" opacity="0.35"/>
    <polygon points="849,690 425,640 560,760 849,770" fill="#ffffff" opacity="0.12"/>
  </svg>

  <div class="sign">
    <svg class="sign-hanger" viewBox="0 0 320 215" aria-hidden="true">
      <line x1="0" y1="10" x2="320" y2="10" stroke="#8c8c8c" stroke-width="6"/>
      <line x1="60" y1="10" x2="60" y2="42" stroke="#8c8c8c" stroke-width="3"/>
      <line x1="260" y1="10" x2="260" y2="42" stroke="#8c8c8c" stroke-width="3"/>
    </svg>
    <div class="sign-board">
      <span class="brand-name">Smooth on<br>the Corner</span>
      <span class="brand-dot"></span>
    </div>
  </div>

  <section class="offer">
    <h1 class="offer-title">FIRST TIME GUEST?</h1>
    <p class="offer-subtitle">ENJOY A COMPLIMENTRY WAX</p>
    <ul class="offer-list">
      <li class="offer-item">For her- indulge in a brow,underarm or bikini line wax</li>
      <li class="offer-item">For him-go smooth with a free ear,nose or brow wax</li>
    </ul>
  </section>
</main>
</body>
</html>
```